Fun, easy to read post card design

Brindle Networks is looking for a designer to create a new (within theme) postcard design.

We have new internet packages rolling out and need to advertise it. Attached is a snippet from our website displaying those new internet plans, our logo and font.

https://www.brindlenetworks.ca/residential/

We would like the focus phrase to be "Fast, local reliable internet"

Let's see what you can come up with!

```html
<!DOCTYPE html>
<html lang="en">
<head>
<meta charset="utf-8">
<title>Brindle Networks – Internet Plans Postcard</title>
<link rel="stylesheet" href="https://fonts.googleapis.com/css2?family=Arimo:wght@400;700&family=Montserrat:ital,wght@1,900&display=swap">
<style>
  :root{
    --page:#1a5788;
    --white:#ffffff;
    --panel-grey:#ececec;
    --ink:#2b2b2b;
    --silver:#1a5486;
    --gold:#1670ad;
    --platinum:#2384cc;
    --advanced:#1fa8d8;
    --unlimited:#5bbfee;
    --hero-blue-1:#0096dc;
    --hero-blue-2:#0a5fc4;
    --footer-dark:#0b1a33;
  }
  *{box-sizing:border-box;margin:0;padding:0}
  html,body{width:1200px;height:1200px;overflow:hidden;background:var(--page)}
  .postcard{position:absolute;left:75px;top:225px;width:1050px;height:750px;background:var(--white);overflow:hidden;font-family:"Arimo",Arial,sans-serif;color:var(--ink)}

  .hero{position:absolute;left:0;top:0;width:1050px;height:261px}
  .hero-photo{position:absolute;left:0;top:0;width:620px;height:261px;background:linear-gradient(100deg,#9a9a9a 0%,#d9d6d2 30%,#efece8 55%,#8d8780 100%)}
  .hero-panel{position:absolute;left:0;top:0}
  .brand{position:absolute;left:48px;top:86px;display:flex;align-items:center;gap:10px;font-family:"Arimo",Arial,sans-serif;font-weight:700;font-size:22px;color:var(--white)}
  .brand-dot{width:26px;height:26px;border-radius:50%;background:var(--advanced)}
  .headline{position:absolute;left:560px;width:432px;top:62px;text-align:center;font-family:"Montserrat",Arial,sans-serif;font-style:italic;font-weight:900;font-size:36px;line-height:38px;color:var(--white);letter-spacing:.5px}
  .tagline{position:absolute;left:560px;width:432px;top:145px;text-align:center;font-size:18.5px;line-height:21px;color:var(--white)}

  .plans{position:absolute;left:76px;top:291px;display:flex;gap:9px}
  .plan{position:relative;width:173px;height:309px}
  .plan-name{height:72px;display:flex;align-items:center;justify-content:center;color:var(--white);font-weight:700;font-size:21px;letter-spacing:.3px}
  .plan-specs{height:190px;background:var(--panel-grey);text-align:center;padding-top:15px}
  .spec-label{font-size:16px;line-height:20px}
  .spec-value{font-weight:700;font-size:17px;line-height:20px;letter-spacing:.5px;margin-bottom:9px}
  .price{position:absolute;left:50%;transform:translateX(-50%);top:245px;width:120px;height:64px;border-radius:4px 4px 24px 24px;color:var(--white);text-align:center}
  .price-amount{font-weight:700;font-size:30px;line-height:36px;padding-top:2px}
  .price-term{font-size:14px;line-height:18px}
  .plan.wide .price{width:140px}

  .silver .plan-name,.silver .price{background:var(--silver)}
  .gold .plan-name,.gold .price{background:var(--gold)}
  .platinum .plan-name,.platinum .price{background:var(--platinum)}
  .advanced .plan-name,.advanced .price{background:var(--advanced)}
  .unlimited .plan-name,.unlimited .price{background:var(--unlimited)}

  .footer{position:absolute;left:0;top:626px;width:1050px;height:124px}
  .footer-art{position:absolute;left:0;top:0}
  .cta{position:absolute;left:290px;width:700px;top:16px;text-align:center;font-family:"Montserrat",Arial,sans-serif;font-style:italic;font-weight:900;font-size:31px;color:var(--white);white-space:nowrap}
  .website{position:absolute;left:290px;width:700px;top:57px;text-align:center;font-weight:700;font-size:20px;color:var(--white)}
</style>
</head>
<body>
<main class="postcard">
  <section class="hero">
    <div class="hero-photo" role="img" aria-label="Photo of a smiling woman in a striped blouse using a smartphone, with colleagues beside her"></div>
    <svg class="hero-panel" width="1050" height="261" viewBox="0 0 1050 261" role="img" aria-label="Blue fibre-optic light background">
      <defs>
        <linearGradient id="heroBlue" x1="0" y1="0" x2="1" y2="1">
          <stop offset="0" stop-color="#00a6e6"/>
          <stop offset="1" stop-color="#0a5fc4"/>
        </linearGradient>
      </defs>
      <polygon points="530,0 560,0 500,130 560,261 530,261 470,130" fill="#ffffff" opacity=".25"/>
      <polygon points="602,0 1050,0 1050,261 602,261 540,130" fill="url(#heroBlue)"/>
    </svg>
    <div class="brand"><span class="brand-dot"></span>Brindle Networks</div>
    <h1 class="headline">FAST, LOCAL,<br>RELIABLE INTERNET</h1>
    <p class="tagline">We create specially tailored coverage plans<br>that provide your home or business<br>with exactly what it needs.</p>
  </section>

  <section class="plans">
    <article class="plan silver">
      <h2 class="plan-name">SILVER</h2>
      <div class="plan-specs">
        <p class="spec-label">Donwload Speed</p><p class="spec-value">10 Mbps</p>
        <p class="spec-label">Upload Speed</p><p class="spec-value">2 Mbps</p>
        <p class="spec-label">Monthly Data</p><p class="spec-value">250GB</p>
      </div>
      <div class="price"><p class="price-amount">$69.95</p><p class="price-term">per month</p></div>
    </article>
    <article class="plan gold">
      <h2 class="plan-name">GOLD</h2>
      <div class="plan-specs">
        <p class="spec-label">Donwload Speed</p><p class="spec-value">20 Mbps</p>
        <p class="spec-label">Upload Speed</p><p class="spec-value">3 Mbps</p>
        <p class="spec-label">Monthly Data</p><p class="spec-value">500GB</p>
      </div>
      <div class="price"><p class="price-amount">$79.95</p><p class="price-term">per month</p></div>
    </article>
    <article class="plan platinum">
      <h2 class="plan-name">PLATINUM</h2>
      <div class="plan-specs">
        <p class="spec-label">Donwload Speed</p><p class="spec-value">30 Mbps</p>
        <p class="spec-label">Upload Speed</p><p class="spec-value">4 Mbps</p>
        <p class="spec-label">Monthly Data</p><p class="spec-value">1000GB</p>
      </div>
      <div class="price"><p class="price-amount">$94.95</p><p class="price-term">per month</p></div>
    </article>
    <article class="plan advanced">
      <h2 class="plan-name">ADVANCED</h2>
      <div class="plan-specs">
        <p class="spec-label">Donwload Speed</p><p class="spec-value">35 Mbps</p>
        <p class="spec-label">Upload Speed</p><p class="spec-value">5 Mbps</p>
        <p class="spec-label">Monthly Data</p><p class="spec-value">1200GB</p>
      </div>
      <div class="price"><p class="price-amount">$99.95</p><p class="price-term">per month</p></div>
    </article>
    <article class="plan unlimited wide">
      <h2 class="plan-name">UNLIMITED</h2>
      <div class="plan-specs">
        <p class="spec-label">Donwload Speed</p><p class="spec-value">35 Mbps</p>
        <p class="spec-label">Upload Speed</p><p class="spec-value">5 Mbps</p>
        <p class="spec-label">Monthly Data</p><p class="spec-value">1200GB</p>
      </div>
      <div class="price"><p class="price-amount">$149.95</p><p class="price-term">per month</p></div>
    </article>
  </section>

  <section class="footer">
    <svg class="footer-art" width="1050" height="124" viewBox="0 0 1050 124" role="img" aria-label="Dark fibre-optic light background with blue glow">
      <defs>
        <linearGradient id="footDark" x1="0" y1="0" x2="1" y2="1">
          <stop offset="0" stop-color="#1a2f6a"/>
          <stop offset=".5" stop-color="#0b1a33"/>
          <stop offset="1" stop-color="#0d2c4f"/>
        </linearGradient>
        <linearGradient id="footBlue" x1="0" y1="0" x2="1" y2="1">
          <stop offset="0" stop-color="#0a7fd6"/>
          <stop offset="1" stop-color="#0a5fc4"/>
        </linearGradient>
      </defs>
      <rect width="1050" height="124" fill="url(#footDark)"/>
      <polygon points="0,0 290,0 340,62 290,124 0,124" fill="#4a8fd0" opacity=".45"/>
      <polygon points="0,0 270,0 320,62 270,124 0,124" fill="url(#footBlue)"/>
    </svg>
    <p class="cta">SIGN UP NOW or CALL 1-780-555-0148</p>
    <p class="website">www.brindlenetworks.ca</p>
  </section>
</main>
</body>
</html>
```